Flyer-Design für traditionelles Dorffest
Zielgruppe
Benötigen Flyer/Plakat design A4 Doppelseite für traditionelles Dorffest.
Aufgabenstellung
Das Design soll einem traditionellen Dorffest der Schützenkompanie entsprechen. (Farben: Dunkelgrün oder Rot / Weiß)
Text Vorderseite:
- Die Schützenkompanie Obermoosbach lädt zum Obermoosbacher Dorffest. (Überschrift Obermoosbacher Dorffest groß)
- Samstag 10. August 2019
- Erstmals mit 'Riesen-Fußball-Dart' Turnier ab 14 Uhr
- 17 Uhr Einmarsch der Musikkapelle Obermoosbach mit anschließendem Konzert im Festzelt
- Stimmungsabend mit 'Die fesch'n Gamsler'
- zugestellt durch briefweg.at an einen Haushalt (Kleiner Hinweiß rechts oben)
- Eintritt: 5€ (Kleiner Schriftzug)
- Mit Schießbude, Wein- und Kaffeebar, Weißbierbar, Schützenbar und großer Tombola
Logos Vorderseite:
- Logo Musik 'Die fesch'n Gamsler'.
- Tiroler Adler (Schützen) Eventuell im Hintergrund oder Modifizieren
- Eventuell Bild von Hinterthiersee mit einbauchen (Hintergrund)
Text Hinterseite:
- Überschrift groß: 'Riesen-Fußball-Dart' Turnier
- Beginn um 14 Uhr
- 3 Spieler pro Team
- Startgebühr: 30 € pro Team (Damen, Herren oder Mixed Teams möglich) / Kinderteams 15 €
- Für Unfälle jeglicher Art wird vom Veranstalter keine Haftung übernommen! (Kleine Schrift)
- Wir achten auf den Jugendschutz! (Kleine Schrift)
- Überschrift groß: 'Heimfahrservice innerhalb von Moosbachtal'
Auf Euer Kommen freut sich die Schützenkompanie Obermoosbach!
Logos Rückseite Sponsoren: Kornkasse Bergtal, Laufwerker Obermoosbach, Jausenstation Brunnalm, Loidlmayr Bau, Metzgerei Stangl, Zitherbau Egger, varolin GmbH, Sanitär Technik Aubing
Logos im Anhang. Foto von Hinterthiersee und Tiroler Adler bei Bedarf via Mail (Da nicht mehr Anhänge möglich sind).
Bei Fragen freue Ich mich über Ihre Nachricht.
Vielen Dank für die Vorschläge.

```html
<!DOCTYPE html>
<html lang="de">
<head>
<meta charset="utf-8">
<title>Obermoosbacher Dorffest – Flyer</title>
<link href="https://fonts.googleapis.com/css2?family=Luckiest+Guy&family=Roboto:ital,wght@0,400;0,500;0,700;0,900;1,400&display=swap" rel="stylesheet">
<style>
:root{
  --board-light:#eff0f0;
  --board-grey:#d4d5d7;
  --green:#3a9647;
  --green-dark:#2c7f39;
  --green-line:#46ad52;
  --navy:#0f2f3c;
  --red:#c8292a;
  --red-title:#cf2b2b;
  --white:#ffffff;
  --ink:#1d1d1d;
  --head:"Luckiest Guy","Arial Black",Impact,sans-serif;
  --body:"Roboto",Arial,sans-serif;
}
*{box-sizing:border-box;margin:0;padding:0}
html,body{width:1200px;height:2670px;overflow:hidden}
body{
  position:relative;font-family:var(--body);color:var(--ink);
  background:linear-gradient(var(--board-light) 0 720px,var(--board-grey) 720px 100%);
}
.board-title{
  position:absolute;top:106px;left:0;width:1200px;text-align:center;
  font-family:var(--head);font-weight:900;text-transform:uppercase;color:var(--red-title);
  font-size:64px;line-height:66px;letter-spacing:1px;white-space:nowrap;
}
.page{
  position:absolute;left:242px;width:716px;background:var(--green);overflow:hidden;
  box-shadow:4px 6px 10px rgba(0,0,0,.35);
}
.page--front{top:294px;height:1012px}
.page--back{top:1362px;height:1010px}
.page-header{position:absolute;left:0;top:0;width:100%;height:132px;background:var(--white);border-bottom:5px solid var(--green-line)}
.band-logo{position:absolute;font-weight:700;font-size:22px;color:var(--ink);white-space:nowrap}
.band-logo--main{left:354px;top:52px;transform:translateX(-50%);font-size:26px}
.delivery-note{position:absolute;right:25px;top:34px;text-align:right;font-size:14px;line-height:18px;color:var(--ink)}
.delivery-note b{font-weight:700}
.front-stage{
  position:absolute;left:0;top:137px;width:100%;height:661px;
  background:radial-gradient(circle at 50% 60%,#45a553 0,var(--green) 45%,var(--green-dark) 100%);
}
.front-base{position:absolute;left:0;top:798px;width:100%;height:214px;background:var(--navy)}
.invite{position:absolute;top:200px;width:100%;text-align:center;color:var(--white);font-size:19px;font-weight:500}
.fest-title{
  position:absolute;top:230px;width:100%;text-align:center;color:var(--white);
  font-family:var(--head);font-weight:900;text-transform:uppercase;
  font-size:58px;line-height:70px;letter-spacing:1px;white-space:nowrap;
}
.date-stamp{
  position:absolute;left:50px;top:412px;width:166px;height:160px;border:3px dashed var(--white);
  transform:rotate(-9deg);color:var(--white);text-align:center;font-weight:700;
}
.date-stamp .day{font-size:26px;margin-top:10px;letter-spacing:1px}
.date-stamp .num{font-size:46px;line-height:44px;color:var(--navy)}
.date-stamp .year{font-size:50px;line-height:52px}
.music-art{position:absolute;left:282px;top:388px;width:166px;height:268px;border-radius:40px;background:linear-gradient(#7cc386,#5fb06b);opacity:.55}
.entry{position:absolute;left:520px;top:572px;display:flex;align-items:center;color:var(--white);font-weight:700;font-size:20px}
.entry-price{margin-left:8px;width:58px;height:58px;border-radius:50%;background:var(--red);display:flex;align-items:center;justify-content:center;font-size:32px;font-weight:900}
.entry-price small{font-size:18px}
.entry-hint{position:absolute;left:532px;top:634px;color:var(--white);font-size:14px;font-weight:500}
.program{position:absolute;left:58px;top:660px;width:599px;height:298px;background:var(--red);color:var(--white);border-left:4px solid #a91f20}
.program-title{position:absolute;top:18px;left:0;width:100%;text-align:center;font-size:20px;font-weight:500}
.program-title span{display:inline-block;padding:0 18px 4px;border-bottom:2px solid var(--white)}
.slot{position:absolute;left:17px;display:flex;align-items:flex-start}
.slot-time{width:132px;font-size:28px;font-weight:700;white-space:nowrap}
.slot-time small{font-size:15px}
.slot-text{font-size:13px;font-weight:500;line-height:17px}
.slot-text b{font-size:17px;font-weight:700}
.slot--one{top:72px}
.slot--one .slot-text{padding-top:10px}
.slot--two{top:138px}
.slot--two .slot-text{padding-top:4px}
.program-extras{position:absolute;bottom:22px;width:100%;text-align:center;font-size:13px;font-weight:500}
.sponsor-row{position:absolute;left:0;width:100%;display:flex;align-items:center;justify-content:space-around;padding:0 20px}
.sponsor{display:flex;align-items:center;gap:8px;font-weight:700;font-size:17px;color:var(--ink);white-space:nowrap}
.sponsor .mark{width:26px;height:26px;background:#f1d300}
.sponsor .dot{width:22px;height:22px;border-radius:50%;background:var(--red)}
.sponsor--green{color:#2b8a3b}
.sponsor--blue{color:#1f6bc4}
.back-header .sponsor-row{top:0;height:127px}
.back-stage{position:absolute;left:0;top:132px;width:100%;height:745px;background:linear-gradient(160deg,#3f9c4b,var(--green-dark))}
.back-title{
  position:absolute;top:158px;width:100%;text-align:center;color:var(--white);
  font-family:var(--head);font-weight:900;text-transform:uppercase;
  font-size:48px;line-height:62px;white-space:nowrap;
}
.target-art{
  position:absolute;left:40px;top:288px;width:496px;height:318px;border-radius:159px;
  background:linear-gradient(90deg,#3f8f4a 0,#d8432c 45%,#e4583c 100%);opacity:.85;
}
.facts{position:absolute;left:77px;top:626px;color:var(--white);font-weight:700;font-size:22px;display:flex;gap:34px;align-items:baseline;white-space:nowrap}
.facts .big{font-size:34px}
.facts small{font-size:15px}
.signup{position:absolute;left:77px;top:666px;color:var(--white);font-size:17px}
.contacts{position:absolute;left:77px;top:693px;color:var(--white);font-size:18px;display:flex;gap:22px}
.contact{display:flex;align-items:center;gap:5px}
.fine-print{position:absolute;left:77px;top:734px;color:var(--white);font-size:9px;line-height:12px}
.fine-print b{font-weight:700}
.homeride{position:absolute;left:73px;top:782px;color:var(--white);font-size:30px;font-weight:700;white-space:nowrap}
.closing{position:absolute;left:77px;top:822px;color:var(--white);font-size:16px;font-style:italic}
.page-footer{position:absolute;left:0;top:877px;width:100%;height:133px;background:var(--white);border-top:5px solid var(--green-line)}
.page-footer .sponsor-row{top:0;height:128px}
.page-footer .sponsor{font-size:15px}
</style>
</head>
<body>

<h1 class="board-title">Obermoosbacher<br>Dorffest</h1>

<section class="page page--front">
  <div class="front-stage"></div>
  <div class="front-base"></div>
  <header class="page-header">
    <div class="band-logo band-logo--main">Die fesch'n Gamsler</div>
    <p class="delivery-note">zugestellt durch<br><b>briefweg.at</b><br>an einen Haushalt</p>
  </header>
  <p class="invite">Die Schützenkompanie Obermoosbach lädt zum</p>
  <h2 class="fest-title">Obermoosbacher<br>Dorffest</h2>
  <div class="date-stamp">
    <div class="day">SAMSTAG</div>
    <div class="num">10.08</div>
    <div class="year">2019</div>
  </div>
  <div class="music-art" role="img" aria-label="Illustration eines wirbelnden Notenbands mit Violinschlüssel"></div>
  <div class="entry">Eintritt: <span class="entry-price">5<small>€</small></span></div>
  <p class="entry-hint">(Kleiner Schriftzug)</p>
  <div class="program">
    <div class="program-title"><span>PROGRAMM</span></div>
    <div class="slot slot--one">
      <div class="slot-time">14:00 <small>UHR</small></div>
      <div class="slot-text">Erstmals mit <b>'Riesen-Fußball-Dart'</b> Turnier</div>
    </div>
    <div class="slot slot--two">
      <div class="slot-time">17:00 <small>UHR</small></div>
      <div class="slot-text">Einmarsch der Musikkapelle Obermoosbach mit<br>anschließendem Konzert im Festzelt Stimmungsabend<br>mit <b>'Die fesch'n Gamsler'</b><br><br>Stimmungsabend mit <b>'Die fesch'n Gamsler'</b></div>
    </div>
    <p class="program-extras">Mit Schießbude, Wein- und Kaffeebar, Weißbierbar, Schützenbar und großer Tombola</p>
  </div>
</section>

<section class="page page--back">
  <div class="back-stage"></div>
  <header class="page-header back-header">
    <div class="sponsor-row">
      <div class="sponsor">Kornkasse Bergtal <span class="mark"></span></div>
      <div class="sponsor">Laufwerker Obermoosbach</div>
      <div class="sponsor sponsor--green">Jausenstation Brunnalm</div>
    </div>
  </header>
  <h2 class="back-title">Riesen-Fussball-Dart<br>Turnier</h2>
  <div class="target-art" role="img" aria-label="Illustration eines Fußballs vor einer rot-weißen Zielscheibe"></div>
  <div class="facts">
    <span>Beginn um <span class="big">14</span> <small>UHR</small></span>
    <span><span class="big">3</span> Spieler pro Team</span>
  </div>
  <p class="signup">Anmeldungen an:</p>
  <div class="contacts">
    <span class="contact">
      <svg width="18" height="18" viewBox="0 0 18 18"><circle cx="9" cy="9" r="9" fill="#fff"/><rect x="4" y="5.5" width="10" height="7" fill="none" stroke="#3a9647" stroke-width="1.4"/><path d="M4 5.5l5 4 5-4" fill="none" stroke="#3a9647" stroke-width="1.4"/></svg>
      info@enzian-stangl.at
    </span>
    <span class="contact">
      <svg width="18" height="18" viewBox="0 0 18 18"><circle cx="9" cy="9" r="9" fill="#fff"/><path d="M6 4.5l2 2.2-1 1.3c.7 1.4 1.6 2.3 3 3l1.3-1 2.2 2-1.2 1.6C9 13.4 4.6 9 4.4 5.7z" fill="#3a9647"/></svg>
      +43 6801234567
    </span>
  </div>
  <p class="fine-print">Startgebühr: <b>30 €</b> pro Team (Damen, Herren oder Mixed Teams möglich)<br>Kinderteams <b>15 €</b> - Für Unfälle jeglicher Art wird vom Veranstalter keine Haftung übernommen!<br><b>Wir achten auf den Jugendschutz!</b></p>
  <p class="homeride">Heimfahrservice innerhalb von Moosbachtal</p>
  <p class="closing">Auf Euer Kommen freut sich die Schützenkompanie Obermoosbach!</p>
  <footer class="page-footer">
    <div class="sponsor-row">
      <div class="sponsor"><span class="dot"></span>Loidlmayr Bau</div>
      <div class="sponsor">Metzgerei Stangl</div>
      <div class="sponsor sponsor--green">varolin GmbH</div>
      <div class="sponsor sponsor--blue">Sanitär Technik Aubing</div>
    </div>
  </footer>
</section>

</body>
</html>
```